Tarrowby Builders Business Card Design

We require a business Card for a new Building Company called Tarrowby Builders. We are General Builders that specialize in Industrial, Commercial and Domestic building work. We would like to see a design that incorporates Blue ,Red and White as the colour scheme and a design that will highlight a building theme.
(Once this design is achieved will need to incorporate this for the other side of the business which is Tarrowby Joinery )

Contact Information for Business Card

TARROWBY BUILDERS
17 Wendaree Rd Kelvale SA 5371
Mobile 0427390548
Telephone 08 85047316
Marcus Delroy
Director / Supervisor

```html
<!DOCTYPE html>
<html lang="en">
<head>
<meta charset="utf-8">
<title>Tarrowby Builders – Business Card</title>
<link rel="stylesheet" href="https://fonts.googleapis.com/css2?family=Montserrat:wght@400;500;600&display=swap">
<style>
  :root {
    --brand-blue: #0b6db4;
    --card-white: #f1f1f1;
    --panel-grey: #ececec;
    --backdrop: #e4e5e7;
    --text-light: #ffffff;
  }
  * { box-sizing: border-box; margin: 0; padding: 0; }
  html, body {
    width: 1200px; height: 900px; overflow: hidden;
    background: var(--backdrop);
    font-family: "Montserrat", sans-serif;
  }
  .sheet {
    position: relative; width: 1200px; height: 900px;
    display: flex; flex-direction: column; align-items: center; justify-content: center; gap: 50px;
  }
  .card {
    position: relative; width: 560px; height: 320px; overflow: hidden;
    background: var(--card-white);
    box-shadow: 0 6px 18px rgba(0,0,0,0.12);
  }

  /* Front face */
  .card-front__band {
    position: absolute; left: 0; top: 0; width: 100%; height: 210px;
    background: var(--brand-blue);
    display: flex; flex-direction: column; align-items: center; justify-content: flex-end; gap: 16px;
    padding-bottom: 34px;
  }
  .brand-mark {
    width: 34px; height: 34px; border: 3px solid var(--text-light);
  }
  .brand-name {
    color: var(--text-light); font-weight: 600; font-size: 25px; letter-spacing: 0.08em;
  }
  .card-front__person {
    position: absolute; left: 0; top: 210px; width: 100%; height: 110px;
    display: flex; flex-direction: column; align-items: center; justify-content: flex-start; gap: 3px;
    padding-top: 22px;
    color: var(--brand-blue);
  }
  .person-name { font-weight: 600; font-size: 18px; letter-spacing: 0.06em; }
  .person-role { font-weight: 500; font-size: 13px; letter-spacing: 0.06em; }

  /* Back face */
  .card-back__panel {
    position: absolute; left: 0; top: 0; width: 170px; height: 100%;
    background: var(--panel-grey);
  }
  .card-back__band {
    position: absolute; left: 170px; top: 0; right: 0; height: 100%;
    background: var(--brand-blue);
    display: flex; flex-direction: column; justify-content: center; gap: 20px;
    padding-left: 44px; padding-right: 24px;
  }
  .contact-line {
    display: flex; align-items: center; gap: 14px;
    color: var(--text-light); font-size: 12.5px; font-weight: 500; letter-spacing: 0.08em;
    text-transform: uppercase; white-space: nowrap;
  }
  .contact-line svg { width: 14px; height: 14px; flex: none; }
</style>
</head>
<body>
<main class="sheet">
  <section class="card card-front" aria-label="Business card front">
    <div class="card-front__band">
      <span class="brand-mark" aria-hidden="true"></span>
      <h1 class="brand-name">TARROWBY BUILDERS</h1>
    </div>
    <div class="card-front__person">
      <p class="person-name">MARCUS DELROY</p>
      <p class="person-role">Director / Supervisor</p>
    </div>
  </section>

  <section class="card card-back" aria-label="Business card back">
    <div class="card-back__panel"></div>
    <div class="card-back__band">
      <p class="contact-line">
        <svg viewBox="0 0 14 14" fill="none" stroke="#fff" stroke-width="1.4" aria-hidden="true">
          <path d="M7 13 C7 13 2.5 8 2.5 5.2 A4.5 4.5 0 0 1 11.5 5.2 C11.5 8 7 13 7 13Z"/>
          <circle cx="7" cy="5.3" r="1.6"/>
        </svg>
        17 Wendaree Rd Kelvale SA 5371
      </p>
      <p class="contact-line">
        <svg viewBox="0 0 14 14" fill="none" stroke="#fff" stroke-width="1.4" aria-hidden="true">
          <rect x="3.5" y="1" width="7" height="12" rx="1.2"/>
          <line x1="6" y1="11" x2="8" y2="11"/>
        </svg>
        0427390548
      </p>
      <p class="contact-line">
        <svg viewBox="0 0 14 14" fill="#fff" aria-hidden="true">
          <path d="M3 1.5 L5.2 1.2 L6.2 4.2 L4.8 5.3 C5.5 7 6.9 8.4 8.7 9.2 L9.8 7.8 L12.8 8.8 L12.5 11 C12.3 12.1 11.4 12.8 10.3 12.6 C5.9 11.8 2.2 8.1 1.4 3.7 C1.2 2.6 1.9 1.7 3 1.5Z"/>
        </svg>
        08 85047316
      </p>
    </div>
  </section>
</main>
</body>
</html>
```